Ad design for a macarons brand

We are a dessert brand with one product line: macarons. Our products delight. Every bite is a dream!

We are launching a new product and would like to lunch a small tactical campaign for the product to boost sales.

The new macron is mango ganache and the middle a mix of sour mango and yuzu (https://www.plumvarell.com/about-the-fruit-584302).

Here are some images we took of the new macaron
https://www.fennlocker.com/sh/qrtwpzhkvbmls/AAFJtRWD-nxPlkhQZ7CeW4DLp?dl=0

I attach the brand guideline document.

Required sizes

1080 x 1350
1080 x 1920

```html
<!DOCTYPE html>
<html lang="en">
<head>
<meta charset="utf-8">
<title>Merli – Mango Ganache Launch</title>
<link rel="stylesheet" href="https://fonts.googleapis.com/css2?family=Abril+Fatface&family=Montserrat:wght@400&display=swap">
<style>
  :root {
    --canvas: #ffffff;
    --lilac-edge: #d0a6e9;
    --lilac-mid: #dcbdf0;
    --lilac-glow: #f1e4f8;
    --ink: #0d0a10;
    --shadow: #8a8a8a;
    --mango-light: #f2b23f;
    --mango-deep: #c97e1c;
  }
  * { margin: 0; padding: 0; box-sizing: border-box; }
  html, body {
    width: 1200px; height: 1000px; overflow: hidden;
    background: var(--canvas);
  }
  .stage { position: relative; width: 1200px; height: 1000px; }

  .poster {
    position: absolute;
    background: radial-gradient(ellipse at 50% 52%, var(--lilac-glow) 0%, var(--lilac-mid) 55%, var(--lilac-edge) 100%);
    box-shadow: 12px 12px 0 var(--shadow);
    color: var(--ink);
    text-align: center;
    overflow: hidden;
  }
  .poster--story { left: 80px; top: 78px; width: 485px; height: 862px; }
  .poster--feed  { left: 634px; top: 334px; width: 484px; height: 606px; }

  .brand-name {
    position: absolute; left: 0; right: 0;
    font-family: "Montserrat", sans-serif; font-weight: 400;
    line-height: 1; letter-spacing: 2px;
  }
  .artwork { position: absolute; left: 0; top: 0; }
  .flavour-label {
    font-family: "Abril Fatface", serif;
    fill: var(--ink);
  }
  .headline {
    position: absolute; left: 0; right: 0;
    font-family: "Abril Fatface", serif; font-weight: 400;
    white-space: nowrap;
  }

  .poster--story .brand-name { top: 120px; font-size: 104px; }
  .poster--story .headline { top: 574px; font-size: 56px; line-height: 65px; }

  .poster--feed .brand-name { top: 50px; font-size: 86px; }
  .poster--feed .headline { top: 441px; font-size: 47px; line-height: 45px; }
</style>
</head>
<body>
<main class="stage">

  <section class="poster poster--story" aria-label="Mango ganache launch, 1080 by 1920">
    <div class="brand-name">MERLI</div>
    <svg class="artwork" width="485" height="862" viewBox="0 0 485 862">
      <defs>
        <radialGradient id="mango-story" cx="45%" cy="35%" r="65%">
          <stop offset="0%" stop-color="var(--mango-light)"/>
          <stop offset="100%" stop-color="var(--mango-deep)"/>
        </radialGradient>
        <path id="smile-story" d="M 100 430 Q 242 560 380 436"/>
      </defs>
      <ellipse role="img" aria-label="Photo of the mango ganache macaron" cx="242" cy="392" rx="68" ry="55" fill="url(#mango-story)"/>
      <text class="flavour-label" font-size="40">
        <textPath href="#smile-story" startOffset="50%" text-anchor="middle">mango ganache</textPath>
      </text>
    </svg>
    <h1 class="headline">the New Kid<br>on<br>the Block</h1>
  </section>

  <section class="poster poster--feed" aria-label="Mango ganache launch, 1080 by 1350">
    <div class="brand-name">MERLI</div>
    <svg class="artwork" width="484" height="606" viewBox="0 0 484 606">
      <defs>
        <radialGradient id="mango-feed" cx="45%" cy="35%" r="65%">
          <stop offset="0%" stop-color="var(--mango-light)"/>
          <stop offset="100%" stop-color="var(--mango-deep)"/>
        </radialGradient>
        <path id="smile-feed" d="M 120 304 Q 242 414 362 314"/>
      </defs>
      <ellipse role="img" aria-label="Photo of the mango ganache macaron" cx="241" cy="269" rx="58" ry="47" fill="url(#mango-feed)"/>
      <text class="flavour-label" font-size="35">
        <textPath href="#smile-feed" startOffset="50%" text-anchor="middle">mango ganache</textPath>
      </text>
    </svg>
    <h2 class="headline">the New Kid<br>on<br>the Block</h2>
  </section>

</main>
</body>
</html>
```